Business Card Design - Carrington Hill Lodge

We are looking at a new design for our business cards that has a modern and professional look. We run a residential aged care facility focussing on the care of residents. The cards will be used for potential clients, consultants and business opportunities in this sector. Blue and white is our main colours and would to see these colours incorporated in the design.
Industry/Entity Type
Business
Contact Information for Business Card
Carrington Hill Lodge, Darren Pelham, dpelham@carringtonhilllodge.com.au, Finance Manager, 0491 736 208, BCom, 48 Yarrabee Way, Bellmere Vale, Qld 4071.

```html
<!DOCTYPE html>
<html lang="en">
<head>
<meta charset="utf-8">
<title>Carrington Hill Lodge – Business Card</title>
<link rel="stylesheet" href="https://fonts.googleapis.com/css2?family=Raleway:ital,wght@0,400;0,500;0,700;1,500&family=Oswald:wght@400&display=swap">
<style>
  :root{
    --page:#ffffff;
    --frame:#333333;
    --card-light:#f7f9fb;
    --card-mist:#e7ecf0;
    --banner-deep:#255684;
    --banner-bright:#00aeef;
    --banner-rule:#7fd3f5;
    --slate:#4c6170;
    --slate-dark:#2f3e48;
    --slate-soft:#6b8797;
    --ink:#4a5a66;
    --back-bg:#dde4ea;
    --back-band:#b9c5ce;
    --back-ink:#4a5d6b;
    --mark:#567d96;
    --tag:#a69c92;
    --ghost:#dfe5ea;
  }
  html,body{margin:0;padding:0;background:var(--page);overflow:hidden;}
  .canvas{display:block;width:1200px;height:1200px;}
  .card-frame{fill:var(--page);stroke:var(--frame);stroke-width:4;}
  .name{font-family:"Raleway",sans-serif;}
  .contact{font-family:"Raleway",sans-serif;font-size:32px;fill:var(--ink);}
  .ghost-name{font-family:"Oswald",sans-serif;font-size:88px;fill:var(--ghost);letter-spacing:14px;}
  .brand-name{font-family:"Raleway",sans-serif;font-weight:500;font-size:37px;fill:#3e4f5c;letter-spacing:2px;}
  .tagline{font-family:"Raleway",sans-serif;font-style:italic;font-weight:500;font-size:26px;fill:#ffffff;}
</style>
</head>
<body>
<svg class="canvas" viewBox="0 0 1500 1500" width="1200" height="1200" xmlns="http://www.w3.org/2000/svg">
  <defs>
    <linearGradient id="bannerFill" x1="0" y1="0" x2="1" y2="0">
      <stop offset="0" stop-color="var(--banner-deep)"/>
      <stop offset="1" stop-color="var(--banner-bright)"/>
    </linearGradient>
    <linearGradient id="bannerRule" x1="0" y1="0" x2="1" y2="0">
      <stop offset="0" stop-color="var(--banner-rule)"/>
      <stop offset="0.8" stop-color="var(--banner-rule)" stop-opacity="0"/>
    </linearGradient>
    <linearGradient id="vineTone" x1="0" y1="0" x2="1" y2="1">
      <stop offset="0" stop-color="var(--slate)" stop-opacity="0"/>
      <stop offset="1" stop-color="var(--slate-soft)" stop-opacity="0.55"/>
    </linearGradient>
    <linearGradient id="backVineTone" x1="0" y1="0" x2="0" y2="1">
      <stop offset="0" stop-color="#c4ced5" stop-opacity="0.7"/>
      <stop offset="1" stop-color="#c4ced5" stop-opacity="0.2"/>
    </linearGradient>
    <filter id="softShadow" x="-10%" y="-20%" width="130%" height="160%">
      <feDropShadow dx="2" dy="6" stdDeviation="7" flood-color="#000" flood-opacity="0.35"/>
    </filter>
    <clipPath id="frontClip"><rect x="238" y="100" width="1024" height="598"/></clipPath>
  </defs>

  <!-- Front side -->
  <g class="card card-front">
    <rect class="card-frame" x="211" y="73" width="1078" height="652"/>
    <g clip-path="url(#frontClip)">
      <rect x="238" y="100" width="1024" height="598" fill="var(--card-light)"/>
      <rect x="238" y="130" width="800" height="490" fill="var(--card-mist)" opacity="0.55"/>
      <text class="ghost-name" x="230" y="730">CARRINGTON HILL LODGE</text>
      <polygon class="side-panel" points="935,100 1262,100 1262,698 980,698 1118,500" fill="var(--slate)" filter="url(#softShadow)"/>
      <polygon class="panel-ornament" role="img" aria-label="Decorative climbing vine with leaves" points="1060,100 1262,100 1262,698 1085,698 1150,420" fill="url(#vineTone)"/>
      <polygon class="banner-fold" points="1040,325 1094,325 1066,356" fill="var(--slate-dark)"/>
    </g>
    <g class="name-banner">
      <rect x="238" y="162" width="856" height="163" fill="url(#bannerFill)" filter="url(#softShadow)"/>
      <rect x="238" y="278" width="856" height="3" fill="url(#bannerRule)"/>
      <text class="name" x="306" y="262" font-size="60" fill="#fff"><tspan font-weight="400">Darren </tspan><tspan font-weight="700">Pelham</tspan></text>
      <text class="name" x="309" y="309" font-size="22" fill="#fff">Finance Manager</text>
    </g>
    <g class="contact-block">
      <text class="contact" x="287" y="444">Carrington Hill Lodge,</text>
      <text class="contact" x="287" y="483">BCom, 48 Yarrabee Way, Bellmere Vale, Qld 4071.</text>
      <g class="icon-phone" fill="var(--ink)">
        <path d="M290,505 q18,-12 36,0 l0,6 l-8,0 l-2,-5 q-8,-3 -16,0 l-2,5 l-8,0z"/>
        <rect x="294" y="510" width="28" height="14" rx="2"/>
      </g>
      <text class="contact" x="338" y="524">0491 736 208</text>
      <g class="icon-mail">
        <rect x="292" y="538" width="34" height="22" fill="var(--ink)"/>
        <path d="M292,538 l17,13 l17,-13" fill="none" stroke="var(--card-light)" stroke-width="2.5"/>
      </g>
      <text class="contact" x="337" y="562">dpelham@carringtonhilllodge.com.au</text>
    </g>
  </g>

  <!-- Back side -->
  <g class="card card-back">
    <rect class="card-frame" x="211" y="775" width="1078" height="652"/>
    <rect x="238" y="802" width="1024" height="598" fill="var(--back-bg)"/>
    <rect class="corner-ornament" role="img" aria-label="Faint decorative vine in the top left corner" x="238" y="802" width="120" height="400" fill="url(#backVineTone)" opacity="0.5"/>
    <rect class="corner-ornament" role="img" aria-label="Faint decorative vine in the bottom right corner" x="1150" y="930" width="112" height="470" fill="url(#backVineTone)" opacity="0.5"/>
    <g class="brand-lockup">
      <circle cx="750" cy="1010" r="78" fill="var(--mark)"/>
      <text class="brand-name" x="750" y="1146" text-anchor="middle">CARRINGTON HILL LODGE</text>
      <rect x="543" y="1157" width="414" height="42" fill="var(--tag)"/>
      <text class="tagline" x="750" y="1187" text-anchor="middle">Comfort, Respect, Companionship</text>
    </g>
    <g class="name-band">
      <rect x="238" y="1230" width="1024" height="142" fill="var(--back-band)"/>
      <text class="name" x="750" y="1297" text-anchor="middle" font-size="56" fill="var(--back-ink)">Darren Pelham</text>
      <rect x="420" y="1315" width="660" height="2" fill="var(--back-ink)"/>
      <text class="name" x="750" y="1353" text-anchor="middle" font-size="27" fill="var(--back-ink)">Finance Manager</text>
    </g>
  </g>
</svg>
</body>
</html>
```